We need a new design for our construction website

We need a new website for our wordpress site ferncrestworks.co.nz

It needs to be only a few pages but sleek in design and responsive, beautifully showcasing our images and video. Currently we have
1. home
2. about us
3. contact
We need either a front page that is designed much better to showcase more content, or potentially a projects page which has images from our builds. We don't have a lot of content so the content we do have needs to be maximised by image, rather than project.

Target Market(s)

High end residential construction and renovation projects, people wanting to build a nice home, clients based in Mount Maunganui, Tauranga.

Coding

Font styles to use
Sans Serif

Colors

Designer to choose only greyscale colors for use in the design.

Requirements
Must have
• A sleek design, architectural

```html
<!DOCTYPE html>
<html lang="en">
<head>
<meta charset="utf-8">
<title>Ferncrest Works</title>
<link href="https://fonts.googleapis.com/css2?family=Poppins:wght@300;400;500;600;700;800&display=swap" rel="stylesheet">
<style>
:root{
  --ink:#111214;
  --header:#0e0f10;
  --nav-active:#4a4d50;
  --accent:#d3d5d7;
  --accent-line:#a9acaf;
  --divider:#8f9295;
  --white:#ffffff;
  --text:#1c1c1c;
  --hero-a:#35383b;
  --hero-b:#5e6164;
}
*{margin:0;padding:0;box-sizing:border-box}
html,body{width:992px;height:1200px;overflow:hidden;background:var(--white)}
body{font-family:'Poppins',sans-serif;color:var(--text);position:relative}
.hero{position:absolute;left:0;top:0;width:992px;height:618px;
  background:linear-gradient(160deg,var(--hero-a) 0%,var(--hero-b) 45%,#44474a 75%,#25272a 100%)}
.header{position:absolute;left:0;top:0;width:992px;height:87px;background:var(--header)}
.brand{position:absolute;left:118px;top:14px;display:flex;align-items:center;gap:12px}
.brand-mark{width:52px;height:60px;border:2px solid #8a8c8e;border-radius:4px}
.brand-name{font-weight:300;font-size:26px;letter-spacing:11px;color:#9a9c9e}
.nav{position:absolute;top:0;left:0}
.nav a{position:absolute;top:36px;font-size:10px;color:var(--white);text-decoration:none;text-transform:uppercase}
.nav .active{left:474px;top:0;width:91px;height:60px;background:var(--nav-active);display:flex;align-items:center;justify-content:center;padding-top:2px}
.nav .active::after{content:"";position:absolute;left:45px;top:54px;width:1px;height:18px;background:var(--white)}
.search{position:absolute;left:768px;top:29px;width:94px;height:29px;border:1px solid #c8c8c8;border-radius:15px;color:var(--white);font-size:10px;display:flex;align-items:center;justify-content:center}
.hero-copy{position:absolute;left:358px;top:238px;width:320px;text-align:center;color:var(--white)}
.hero-copy h1{font-weight:800;font-size:42px;line-height:62px}
.hero-copy p{font-size:17px;line-height:26px;margin-top:2px}
.btn{position:absolute;background:#000;color:#e8e8e8;font-weight:500;font-size:12.5px;display:flex;align-items:center;justify-content:center;gap:14px}
.btn svg{width:22px;height:8px}
.btn-hero{left:453px;top:428px;width:129px;height:41px}
.slide-arrow{position:absolute;top:308px}
.info-bar{position:absolute;left:119px;top:598px;width:745px;height:46px;background:var(--accent);font-size:9.5px;color:#2a2a2a}
.info-bar .item{position:absolute;top:0;height:46px;display:flex;align-items:center}
.info-bar .divider{position:absolute;top:14px;width:1px;height:18px;background:var(--divider)}
.follow{font-weight:600;font-size:12px;color:#1b1b1b}
.social{width:20px;height:20px;border:1px solid #222;border-radius:50%;margin-left:13px}
.about-title{position:absolute;left:118px;top:756px;font-weight:800;font-size:38px;color:var(--ink);letter-spacing:-0.5px}
.about-rule{position:absolute;left:118px;top:812px;width:68px;height:1px;background:var(--accent-line)}
.about-text{position:absolute;left:118px;top:832px;width:353px;font-size:9.6px;line-height:14.9px;text-align:justify;color:#222}
.btn-read{left:119px;top:1047px;width:129px;height:40px}
.photo-frame{position:absolute;left:489px;top:707px;width:362px;height:392px;border:2px solid var(--accent-line)}
.photo{position:absolute;left:502px;top:721px;width:361px;height:389px;
  background:linear-gradient(170deg,#d0d2d4 0%,#a3a6a9 40%,#5a5d60 75%,#333537 100%)}
</style>
</head>
<body>
  <section class="hero" role="img" aria-label="Upward view of city towers under a cloudy sky"></section>

  <header class="header">
    <div class="brand"><span class="brand-mark"></span><span class="brand-name">FERNCREST</span></div>
    <nav class="nav">
      <a class="active" href="#">Home</a>
      <a href="#" style="left:603px">About</a>
      <a href="#" style="left:693px">Contact</a>
    </nav>
    <div class="search">Search Here</div>
  </header>

  <div class="hero-copy">
    <h1>OUR VISION</h1>
    <p>is to build beautiful, efficient homes with the best building technologies available that our customers are proud to own.</p>
  </div>
  <div class="btn btn-hero">More Info
    <svg viewBox="0 0 22 8"><path d="M0 4h1M3 4h1M6 4h15M17 1l4 3-4 3" stroke="#e8e8e8" stroke-width="1.3" fill="none"/></svg>
  </div>

  <svg class="slide-arrow" style="left:14px" width="52" height="50" viewBox="0 0 52 50">
    <path d="M14 12 A22 22 0 1 1 14 38" fill="none" stroke="#d6d6d6" stroke-width="3.5"/>
    <path d="M0 25h36M26 15l10 10-10 10" fill="none" stroke="#d6d6d6" stroke-width="3.5"/>
  </svg>
  <svg class="slide-arrow" style="left:926px" width="52" height="50" viewBox="0 0 52 50">
    <path d="M38 12 A22 22 0 1 0 38 38" fill="none" stroke="#ffffff" stroke-width="3.5"/>
    <path d="M52 25H16M26 15L16 25l10 10" fill="none" stroke="#ffffff" stroke-width="3.5"/>
  </svg>

  <div class="info-bar">
    <div class="item" style="left:79px">
      <svg width="20" height="20" viewBox="0 0 20 20"><path d="M4 3l3 0 1 4-2 1c1 2 3 4 5 5l1-2 4 1 0 3c-1 1-2 2-4 1C7 15 4 12 3 7 2 5 3 4 4 3z" fill="#1b1b1b"/><path d="M11 4a5 5 0 0 1 5 5M11 1a8 8 0 0 1 8 8" stroke="#1b1b1b" stroke-width="1.3" fill="none"/></svg>
      <span style="margin-left:14px">123-456-7890</span>
    </div>
    <span class="divider" style="left:218px"></span>
    <div class="item" style="left:260px">
      <span class="follow">Follow Us On:</span>
      <span class="social" style="margin-left:8px"></span><span class="social"></span><span class="social"></span>
    </div>
    <span class="divider" style="left:475px"></span>
    <div class="item" style="left:513px">
      <svg width="18" height="22" viewBox="0 0 18 22"><path d="M9 1a6 6 0 0 1 6 6c0 4-6 10-6 10S3 11 3 7a6 6 0 0 1 6-6z" fill="#1b1b1b"/><circle cx="9" cy="7" r="2" fill="var(--accent)"/><ellipse cx="9" cy="19" rx="7" ry="2" fill="none" stroke="#1b1b1b" stroke-width="1.3"/></svg>
      <span style="margin-left:14px;line-height:13px">Lorem ipsum Public 1234,<br>Somestreet NY 0123</span>
    </div>
  </div>

  <h2 class="about-title">ABOUT US</h2>
  <span class="about-rule"></span>
  <p class="about-text">Lorem ipsum dolor sit amet, consectetur adipiscing elit, sed do eiusmod tempor incididunt ut labore et dolore magna aliqua. Ut enim ad minim veniam, quis nostrud exercitation ullamco laboris nisi ut aliquip ex ea commodo consequat. Duis aute irure dolor in reprehenderit in voluptate velit esse cillum dolore eu fugiat nulla pariatur. Excepteur sint occaecat cupidatat non proident, sunt in culpa qui officia deserunt mollit anim id est laborum.Lorem ipsum dolor sit amet, consectetur adipiscing elit, sed do eiusmod tempor incididunt ut labore et dolore magna aliqua. Ut enim ad minim veniam, quis nostrud exercitation ullamco laboris nisi ut aliquip ex ea commodo consequat. Duis aute irure dolor in reprehenderit in voluptate velit esse cillum dolore eu fugiat nulla pariatur. Excepteur sint occaecat cupidatat non proident, sunt in culpa qui officia deserunt mollit anim id est laborum.</p>
  <div class="btn btn-read">Read More
    <svg viewBox="0 0 22 8"><path d="M0 4h1M3 4h1M6 4h15M17 1l4 3-4 3" stroke="#e8e8e8" stroke-width="1.3" fill="none"/></svg>
  </div>

  <div class="photo-frame"></div>
  <div class="photo" role="img" aria-label="Engineers in hard hats looking up at high-rise towers under construction"></div>
</body>
</html>
```